Banner ads for VL that work with same theme as below banners

Love the banner ads below. Need more with attached photos. But use the same wording, font as in below banner ads. Should be VL size 1200/627 so I can use for Trovique and VL. Looking for great ads to use as VL ads. We do lots of ads so it will be worth your time to enter this contest you will be rewarded with a ton of work. Need several banner ads that work together. So maybe 1 of the dresses, 1 of the sweater, 1 of the leggings, 1 of the jacket

Target Market(s)

Women 24-45

Industry/Entity Type

Fashion

Requirements
Must have
• Banner ads that work for VL and Trovique
Nice to have
• Several options to choose from
Should not have
• not sure

```html
<!DOCTYPE html>
<html lang="en">
<head>
<meta charset="UTF-8">
<title>Winter Wear Collection Banner</title>
<link rel="stylesheet" href="https://fonts.googleapis.com/css2?family=Pinyon+Script&family=Bodoni+Moda:wght@400;500&display=swap">
<style>
  :root {
    --bg-light: #e6e2e2;
    --bg-mid: #dcd7d7;
    --frame-outer: #8e8282;
    --frame-inner: #ffffff;
    --script-ink: #6c5a5a;
    --title-ink: #ffffff;
    --button-fill: #9b8a8b;
    --button-edge: #c9bebe;
    --photo-light: #d4d2d2;
    --photo-wall: #bdbcbc;
    --photo-coat: #2b2d2f;
  }
  * { margin: 0; padding: 0; box-sizing: border-box; }
  html, body { width: 1200px; height: 627px; overflow: hidden; }
  body { background: var(--bg-light); }
  .banner {
    position: relative;
    width: 1200px;
    height: 627px;
    overflow: hidden;
    background: radial-gradient(ellipse at 35% 45%, var(--bg-light) 0%, var(--bg-mid) 100%);
  }
  .model-photo {
    position: absolute;
    left: 700px;
    top: 0;
    width: 500px;
    height: 627px;
    background:
      radial-gradient(ellipse 210px 330px at 215px 400px, var(--photo-coat) 0%, var(--photo-coat) 60%, rgba(43,45,47,0) 100%),
      linear-gradient(90deg, rgba(220,215,215,0) 0%, var(--photo-wall) 10%, var(--photo-light) 60%, var(--photo-light) 100%);
  }
  .title-frame {
    position: absolute;
    left: 84px;
    top: 185px;
    width: 575px;
    height: 157px;
    border: 1px solid var(--frame-outer);
  }
  .title-frame::after {
    content: "";
    position: absolute;
    inset: 4px;
    border: 1px solid var(--frame-inner);
  }
  .title-script {
    position: absolute;
    left: 14px;
    top: 18px;
    font-family: "Pinyon Script", cursive;
    font-size: 54px;
    line-height: 1;
    color: var(--script-ink);
  }
  .title-caps {
    position: absolute;
    left: 19px;
    top: 84px;
    font-family: "Bodoni Moda", serif;
    font-size: 42px;
    line-height: 1;
    letter-spacing: 2px;
    color: var(--title-ink);
  }
  .shop-button {
    position: absolute;
    left: 330px;
    top: 377px;
    width: 329px;
    height: 73px;
    background: var(--button-fill);
    border: 1px solid var(--frame-outer);
    display: flex;
    align-items: center;
    justify-content: center;
    font-family: "Bodoni Moda", serif;
    font-size: 19px;
    letter-spacing: 1.5px;
    color: var(--title-ink);
    text-decoration: none;
  }
  .shop-button::after {
    content: "";
    position: absolute;
    inset: 4px;
    border: 1px solid var(--button-edge);
  }
</style>
</head>
<body>
  <div class="banner">
    <div class="model-photo" role="img" aria-label="Model in a black quilted puffer jacket with faux fur hood and grey knit hem, against a grey concrete wall"></div>
    <div class="title-frame">
      <h1 class="title-script">Winter Wear</h1>
      <p class="title-caps">COLLECTION</p>
    </div>
    <a class="shop-button" href="#">SHOP THE SEASON</a>
  </div>
</body>
</html>
```